Cards and what not
Project: Stationary
Stationary - Consulting
Stationary
Simple
Tomaso Reyk Halden
CEO
Do not want to use an address please.
833-LUMACORP (833-586-2267)
th@lumacorp.com
www.lumacorp.com
Please make the font large enough to more easily read. Some cards...the font is too small. Please use our logo as well. I prefer a vertical design but open to horizontal too. Many thanks :)
lumacorp lumacorp
I am looking for a vertical design while open to checking out horizontal designs (for the business card). Thanks guys (and ladies)

```html
<!DOCTYPE html>
<html lang="en">
<head>
<meta charset="utf-8">
<title>Lumacorp Business Card</title>
<link rel="stylesheet" href="https://fonts.googleapis.com/css2?family=Cinzel:wght@400&family=Open+Sans:wght@400;600&display=swap">
<style>
  :root {
    --bg: #ecebe8;
    --card: #ffffff;
    --cyan: #2bb3e6;
    --grey-band: #b9bbbe;
    --ink: #4a5257;
    --ink-soft: #7d868c;
  }
  * { box-sizing: border-box; margin: 0; padding: 0; }
  html, body {
    width: 1200px; height: 978px; overflow: hidden;
    background: var(--bg);
    font-family: "Open Sans", sans-serif;
  }
  .stage {
    width: 1200px; height: 978px;
    display: flex; align-items: center; justify-content: center; gap: 60px;
  }
  .card {
    position: relative;
    width: 520px; height: 297px;
    background: var(--card);
    border-radius: 22px;
    overflow: hidden;
    box-shadow: 0 10px 30px rgba(0,0,0,0.18);
  }
  .card__band-grey {
    position: absolute; left: 0; right: 0; bottom: 30px; height: 8px;
    background: var(--grey-band);
  }
  .card__band-cyan {
    position: absolute; left: 0; right: 0; bottom: 0; height: 30px;
    background: var(--cyan);
  }
  .brand {
    font-family: "Cinzel", serif;
    font-weight: 400;
    color: var(--cyan);
    letter-spacing: 3px;
    display: flex; align-items: center; gap: 10px;
  }
  .brand__dot {
    width: 14px; height: 14px; border-radius: 50%;
    background: var(--cyan);
  }
  /* contact side */
  .card--contact .brand {
    position: absolute; left: 36px; top: 160px;
    font-size: 30px;
  }
  .contact {
    position: absolute; left: 280px; top: 34px; right: 26px;
    border-left: 2px solid var(--cyan);
    padding-left: 18px;
  }
  .contact__name {
    font-size: 17px; font-weight: 600; color: var(--cyan);
  }
  .contact__title {
    font-size: 13px; color: var(--ink-soft); margin-top: 2px;
    padding-bottom: 10px; border-bottom: 2px solid var(--cyan);
    margin-bottom: 12px;
  }
  .contact__row {
    display: flex; align-items: center; gap: 8px;
    font-size: 12.5px; color: var(--ink);
    margin-bottom: 8px;
  }
  .contact__icon {
    width: 16px; height: 16px; flex: none;
  }
  /* logo side */
  .card--logo .brand {
    position: absolute; left: 0; right: 0; top: 110px;
    justify-content: center;
    font-size: 40px;
  }
</style>
</head>
<body>
<main class="stage">
  <section class="card card--contact" aria-label="Card back, contact details">
    <div class="brand"><span class="brand__dot"></span>LUMACORP</div>
    <div class="contact">
      <p class="contact__name">Tomaso Reyk Halden</p>
      <p class="contact__title">CEO</p>
      <p class="contact__row">
        <svg class="contact__icon" viewBox="0 0 16 16"><circle cx="8" cy="8" r="8" fill="var(--cyan)"/><path d="M5.2 4.3l1.5-.3.8 2-1 .7a5 5 0 0 0 2.8 2.8l.7-1 2 .8-.3 1.5c-3.5.3-6.8-3-6.5-6.5z" fill="#fff"/></svg>
        833-LUMACORP
      </p>
      <p class="contact__row">
        <svg class="contact__icon" viewBox="0 0 16 16"><circle cx="8" cy="8" r="8" fill="var(--cyan)"/><path d="M5.2 4.3l1.5-.3.8 2-1 .7a5 5 0 0 0 2.8 2.8l.7-1 2 .8-.3 1.5c-3.5.3-6.8-3-6.5-6.5z" fill="#fff"/></svg>
        (833-586-2267)
      </p>
      <p class="contact__row">
        <svg class="contact__icon" viewBox="0 0 16 16"><circle cx="8" cy="8" r="8" fill="var(--cyan)"/><rect x="4" y="5" width="8" height="6" fill="none" stroke="#fff" stroke-width="1.2"/><path d="M4 5l4 3.3L12 5" fill="none" stroke="#fff" stroke-width="1.2"/></svg>
        th@lumacorp.com
      </p>
      <p class="contact__row">
        <svg class="contact__icon" viewBox="0 0 16 16"><circle cx="8" cy="8" r="8" fill="var(--cyan)"/><circle cx="8" cy="8" r="4" fill="none" stroke="#fff" stroke-width="1.1"/><path d="M4 8h8M8 4c-2 2.4-2 5.6 0 8M8 4c2 2.4 2 5.6 0 8" fill="none" stroke="#fff" stroke-width="1"/></svg>
        www.lumacorp.com
      </p>
    </div>
    <div class="card__band-grey"></div>
    <div class="card__band-cyan"></div>
  </section>

  <section class="card card--logo" aria-label="Card front, logo">
    <div class="brand"><span class="brand__dot"></span>LUMACORP</div>
    <div class="card__band-grey"></div>
    <div class="card__band-cyan"></div>
  </section>
</main>
</body>
</html>
```